Website for Party

Design a new website for PlumtreeGatherings.net
We have attached the new logos and please look at the website, and our facebook page: facebook.com/plumtreegatherings for inspiration
Updates

Hi Guys, please be original with all designs and images otherwise the design will be eliminated Thank you

some of your designs have too much happening in them, others make it clear that the designer has not yet read the brief fully

Please everyone be original!

```html
<!DOCTYPE html>
<html lang="en">
<head>
<meta charset="utf-8">
<title>Plumtree Gatherings</title>
<link href="https://fonts.googleapis.com/css2?family=Open+Sans:wght@300;400;600;700&family=Josefin+Sans:wght@700&display=swap" rel="stylesheet">
<style>
:root{
  --blue:#0557dc;
  --blue-dark:#003a9e;
  --blue-title:#0a47bd;
  --button:#0a45c2;
  --button-edge:#062f8a;
  --black:#000;
  --text:#444;
  --white:#fff;
  --grey:#cfcfcf;
}
*{margin:0;padding:0;box-sizing:border-box}
html,body{width:1200px;height:1127px;overflow:hidden;background:var(--white)}
body{position:relative;font-family:"Open Sans",sans-serif}
.site-header{position:absolute;left:0;top:0;width:1200px;height:84px;background:var(--blue);z-index:3}
.brand{position:absolute;left:171px;top:0;width:200px;height:197px;z-index:4}
.brand svg{position:absolute;left:0;top:0}
.brand-name{position:absolute;left:0;top:78px;width:200px;text-align:center;color:var(--white);font-family:"Open Sans",sans-serif;font-weight:600;font-size:25px;letter-spacing:1px}
.main-nav{position:absolute;left:522px;top:0;display:flex;height:84px}
.main-nav a{display:flex;align-items:center;height:84px;padding:0 16px;color:var(--white);text-decoration:none;font-weight:600;font-size:15.5px;border-right:1px solid rgba(255,255,255,.18)}
.main-nav a:first-child{border-left:1px solid rgba(0,0,0,.2)}
.main-nav a.is-active{background:var(--blue-dark);border-bottom:3px solid var(--black)}
.hero{position:absolute;left:0;top:84px;width:1200px;height:574px;
  background:linear-gradient(100deg,#6b5a4a 0%,#4a2a55 25%,#3a1e4a 45%,#6a3a6a 60%,#b4584f 80%,#d28a5a 100%)}
.hero-title{position:absolute;left:0;top:196px;width:1200px;text-align:center;color:var(--white);font-family:"Josefin Sans",sans-serif;font-weight:700;font-size:40px;letter-spacing:.5px}
.btn{display:flex;align-items:center;justify-content:center;width:170px;height:46px;background:var(--button);border-bottom:3px solid var(--button-edge);color:#e8eeff;font-size:17px;text-decoration:none}
.hero .btn{position:absolute;left:515px;top:264px}
.slide-arrow{position:absolute;top:264px;width:47px;height:47px;background:#3c3c3c;display:flex;align-items:center;justify-content:center}
.slide-arrow.prev{left:17px}
.slide-arrow.next{left:1136px}
.social-bar{position:absolute;left:1142px;top:518px;width:37px;z-index:2}
.social-bar a{display:flex;align-items:center;justify-content:center;width:37px;height:37px;margin-bottom:2px;background:var(--blue)}
.social-bar span{width:10px;height:10px;background:var(--white)}
.welcome{position:absolute;left:0;top:700px;width:1200px;text-align:center}
.welcome h1{color:var(--blue-title);font-weight:700;font-size:32px;letter-spacing:.3px}
.divider{display:block;margin:8px auto 0}
.welcome p{width:760px;margin:16px auto 0;color:var(--text);font-weight:300;font-size:16.3px;line-height:25.7px}
.welcome .btn{margin:27px auto 0}
.footer-band{position:absolute;left:0;top:1030px}
</style>
</head>
<body>
<header class="site-header">
  <nav class="main-nav">
    <a class="is-active" href="#">WELCOME</a>
    <a href="#">ABOUT</a>
    <a href="#">FAQ</a>
    <a href="#">ORDER TICKETS</a>
    <a href="#">CONTACT</a>
  </nav>
</header>
<div class="brand">
  <svg width="200" height="197" viewBox="0 0 200 197"><polygon points="0,0 200,0 200,146 100,197 0,146" fill="#000"/></svg>
  <div class="brand-name">Plumtree</div>
</div>

<section class="hero" role="img" aria-label="Bartender pouring beer from a chrome tap into a glass">
  <h2 class="hero-title">PREMIUM OPEN BAR TO ENJOY</h2>
  <a class="btn" href="#">READ MORE</a>
  <a class="slide-arrow prev" href="#" aria-label="Previous slide"><svg width="16" height="20" viewBox="0 0 16 20"><polyline points="12,2 4,10 12,18" fill="none" stroke="#111" stroke-width="4"/></svg></a>
  <a class="slide-arrow next" href="#" aria-label="Next slide"><svg width="16" height="20" viewBox="0 0 16 20"><polyline points="4,2 12,10 4,18" fill="none" stroke="#111" stroke-width="4"/></svg></a>
</section>

<aside class="social-bar">
  <a href="#" aria-label="Chirpbook"><span></span></a>
  <a href="#" aria-label="Tweetline"><span></span></a>
  <a href="#" aria-label="Social profile"><span></span></a>
  <a href="#" aria-label="Photo profile"><span></span></a>
  <a href="#" aria-label="Photo stream"><span></span></a>
</aside>

<section class="welcome">
  <h1>WELCOME TO PLUMTREE GATHERINGS</h1>
  <svg class="divider" width="362" height="22" viewBox="0 0 362 22">
    <line x1="0" y1="11" x2="165" y2="11" stroke="#ccc"/>
    <line x1="200" y1="11" x2="362" y2="11" stroke="#ccc"/>
    <polygon points="181,1 184,8.5 192,8.8 185.8,13.7 188,21 181,16.8 174,21 176.2,13.7 170,8.8 178,8.5" fill="#888"/>
  </svg>
  <p>Here at Plumtree, webring the most talented artists to spectacular venues of the Greater NYC area for you to enjoy! We are excited to launch our summer events and parties beginning on the July 4th week-end, 2014.&nbsp; So join us at our exclusive Kickoff Yacht Party on Thursday July 3rd, 2014 and follow us on Chirpbook and Tweetline to stay tuned to the latest news and upcoming events.</p>
  <a class="btn" href="#">READ MORE</a>
</section>

<svg class="footer-band" width="1200" height="97" viewBox="0 0 1200 97">
  <polygon points="0,64 1200,5 1200,97 0,97" fill="#000"/>
  <circle cx="598" cy="34" r="30" fill="var(--grey)"/>
  <g stroke="#111" stroke-width="2" fill="none">
    <line x1="598" y1="16" x2="598" y2="52"/>
    <polyline points="592,45 598,52 604,45"/>
    <polyline points="593,16 598,21 603,16"/>
    <polyline points="593,21 598,26 603,21"/>
  </g>
</svg>
</body>
</html>
```